Digital menu Skydiving company

Design Digital menu/pricelist for our company. It can have dynamic components. We are also looking for a Graphic design for all our projects. Our main goals are to look clean/sharp and professional. Information is in psd file

3 packages Violet Plunge, Meadow Journey, And Lantern Voyage. then we have addons and merchandise

Colors
0293ce
34a7d8
ffffff
fbee3f
3377b5
000000
f37122
ec1f27
e34197

Requirements
Must have
• Sorry If I couldn't get my vision across better, Please see really rough design idea attached. one large picture section that rotates through 3 or 4 pictures. then all the information down the bottom and on right (see menu pricelist attached)

```html
<!DOCTYPE html>
<html lang="en">
<head>
<meta charset="utf-8">
<title>Halcyon Skydive – Packages &amp; Pricing</title>
<link rel="stylesheet" href="https://fonts.googleapis.com/css2?family=Montserrat:wght@300;400;500;700;800&display=swap">
<style>
  :root {
    --blue: #1590cc;
    --blue-deep: #0f86c4;
    --orange: #f37122;
    --ink: #111111;
    --board: #000000;
    --paper: #ffffff;
    --sky-top: #2f56a8;
    --sky-mid: #3d7fc8;
    --sky-low: #a9c6de;
    --canyon: #b98f86;
  }
  * { box-sizing: border-box; margin: 0; padding: 0; }
  html, body { width: 1200px; height: 842px; overflow: hidden; background: var(--board); }
  body { font-family: "Montserrat", sans-serif; color: var(--ink); }

  .menu-board { position: relative; width: 1200px; height: 842px; background: var(--board); }

  .board-header {
    height: 117px; background: var(--paper);
    border-radius: 0 0 34px 34px;
    display: flex; align-items: center; position: relative;
  }
  .brand {
    position: absolute; left: 30px; top: 40px;
    display: flex; align-items: center; gap: 8px;
    font-weight: 800; font-size: 17px; letter-spacing: 1.5px; color: #1b2430;
  }
  .brand-dot { width: 14px; height: 14px; border-radius: 50%; background: var(--blue); }
  .board-title {
    margin-left: 290px; font-weight: 800; font-size: 60px; letter-spacing: 1px;
    color: var(--blue); line-height: 1;
  }

  .packages {
    position: absolute; left: 27px; right: 27px; top: 137px; bottom: 18px;
    display: flex; gap: 30px;
  }
  .package {
    flex: 1; background: var(--paper); border-radius: 26px; overflow: hidden;
    display: flex; flex-direction: column; position: relative;
  }
  .package-head {
    background: var(--blue); color: var(--paper); text-align: center;
    height: 76px; padding-top: 9px;
    font-weight: 800; font-size: 23px; line-height: 1.1; letter-spacing: .5px;
    position: relative;
  }
  .package-head::after {
    content: ""; position: absolute; left: 50%; bottom: -9px; transform: translateX(-50%);
    border-left: 10px solid transparent; border-right: 10px solid transparent;
    border-top: 10px solid var(--blue);
  }
  .package--meadow .package-head { background: var(--orange); }
  .package--meadow .package-head::after { border-top-color: var(--orange); }

  .tagline { text-align: center; font-size: 12.5px; font-weight: 400; margin-top: 17px; letter-spacing: .2px; }

  .features { list-style: none; margin: 14px 18px 0 16px; }
  .feature {
    display: flex; align-items: flex-start; gap: 10px;
    font-weight: 700; font-size: 20px; line-height: 1.22; margin-bottom: 14px;
  }
  .feature .tick { flex: 0 0 16px; margin-top: 4px; }
  .feature-name { flex: 1; }
  .feature-price { font-size: 17px; color: var(--blue); font-weight: 700; align-self: flex-end; }
  .features--tight .feature { margin-bottom: 10px; }

  .price {
    font-weight: 800; color: var(--blue); text-align: center; line-height: 1;
    font-size: 58px; letter-spacing: 1px;
  }
  .package--violet .price { margin-top: 36px; }
  .package--meadow .price { color: var(--orange); margin-top: 4px; }
  .package--lantern .price { margin-top: 40px; }

  .merch { list-style: none; margin: 58px 20px 0 44px; }
  .merch li {
    display: flex; justify-content: space-between;
    font-size: 23px; font-weight: 400; line-height: 1.32; letter-spacing: .3px;
  }

  .package-photo {
    margin-top: auto; height: 242px;
    background: linear-gradient(180deg, var(--sky-top) 0%, var(--sky-mid) 45%, var(--sky-low) 82%, var(--canyon) 100%);
  }
</style>
</head>
<body>
<main class="menu-board">
  <header class="board-header">
    <div class="brand"><span class="brand-dot"></span>HALCYON SKYDIVE</div>
    <h1 class="board-title">PACKAGES &amp; PRICING</h1>
  </header>

  <svg width="0" height="0" style="position:absolute">
    <defs>
      <symbol id="tick" viewBox="0 0 16 16">
        <circle cx="8" cy="8" r="8" fill="currentColor"/>
        <path d="M4.2 8.3l2.5 2.4 5-5" fill="none" stroke="#fff" stroke-width="2" stroke-linecap="round" stroke-linejoin="round"/>
      </symbol>
    </defs>
  </svg>

  <section class="packages">
    <article class="package package--violet">
      <h2 class="package-head">VIOLET PLUNGE<br>16,000FT</h2>
      <p class="tagline">THE SKYDIVE IS NAKED, NOT YOU...</p>
      <ul class="features">
        <li class="feature"><svg class="tick" width="16" height="16" style="color:var(--blue)"><use href="#tick"/></svg><span class="feature-name">TANDEM SKYDIVE FROM 16,000FT MSL</span></li>
        <li class="feature" style="margin-top:22px"><svg class="tick" width="16" height="16" style="color:var(--blue)"><use href="#tick"/></svg><span class="feature-name">CERTIFICATE OF ACHIEVEMENT</span></li>
      </ul>
      <p class="price">$329</p>
      <ul class="merch">
        <li><span>T-Shirt Short Sleeve</span><span>$20</span></li>
        <li><span>T-Shirt Long Sleeve</span><span>$28</span></li>
        <li><span>Sweat Shirts</span><span>$30</span></li>
        <li><span>Hoodies</span><span>$38</span></li>
        <li><span>Goggles from</span><span>$12&nbsp;</span></li>
      </ul>
    </article>

    <article class="package package--meadow">
      <h2 class="package-head">MEADOW JOURNEY<br>16,000FT</h2>
      <p class="tagline">SKYDIVE &amp; SHARE THE MEMORIES...</p>
      <ul class="features">
        <li class="feature"><svg class="tick" width="16" height="16" style="color:var(--orange)"><use href="#tick"/></svg><span class="feature-name">TANDEM SKYDIVE FROM 16,000FT MSL</span></li>
        <li class="feature"><svg class="tick" width="16" height="16" style="color:var(--orange)"><use href="#tick"/></svg><span class="feature-name">PHOTOS</span></li>
        <li class="feature"><svg class="tick" width="16" height="16" style="color:var(--orange)"><use href="#tick"/></svg><span class="feature-name">VIDEOS</span></li>
        <li class="feature"><svg class="tick" width="16" height="16" style="color:var(--orange)"><use href="#tick"/></svg><span class="feature-name">CERTIFICATE OF ACHIEVEMENT</span></li>
      </ul>
      <p class="price">$459</p>
      <div class="package-photo" role="img" aria-label="Tandem skydivers in freefall against a blue sky above a canyon landscape"></div>
    </article>

    <article class="package package--lantern">
      <h2 class="package-head">LANTERN VOYAGE<br>16,000FT</h2>
      <p class="tagline">FOR THE THRILL SEEKER...</p>
      <ul class="features features--tight">
        <li class="feature"><svg class="tick" width="16" height="16" style="color:var(--blue)"><use href="#tick"/></svg><span class="feature-name">TANDEM SKYDIVE FROM 16,000FT MSL</span><span class="feature-price">$319</span></li>
        <li class="feature"><svg class="tick" width="16" height="16" style="color:var(--blue)"><use href="#tick"/></svg><span class="feature-name">PHOTOS</span><span class="feature-price">$99</span></li>
        <li class="feature"><svg class="tick" width="16" height="16" style="color:var(--blue)"><use href="#tick"/></svg><span class="feature-name">VIDEOS</span><span class="feature-price">$99</span></li>
        <li class="feature"><svg class="tick" width="16" height="16" style="color:var(--blue)"><use href="#tick"/></svg><span class="feature-name">EXTREME EXTRAS</span><span class="feature-price">$50</span></li>
        <li class="feature"><svg class="tick" width="16" height="16" style="color:var(--blue)"><use href="#tick"/></svg><span class="feature-name">HALCYON SKYDIVE T-SHIRT</span></li>
        <li class="feature"><svg class="tick" width="16" height="16" style="color:var(--blue)"><use href="#tick"/></svg><span class="feature-name">CERTIFICATE OF ACHIEVEMENT</span></li>
      </ul>
      <p class="price">$499</p>
    </article>
  </section>
</main>
</body>
</html>
```